"Fern Hollow Realty" is the name of my real estate company

This is for a: "for sale" sign, looking for a minimalist design, wire frame outline of a midcentury modern homes roof line or elevation?

My name is: Derek Malloy (needed)
My Cell # is: 555 204 3967 (needed)
My BRE license # is: 04827265 (needed)
BRE needs to be displayed in this format: BRE 04827265 (needed)
The white outline on the sign riders 'pictured" may work on large sign
Note font on pictured rider sign

This design is for a real estate "for sale" sign or sandwich board sign. Do Not include the words "For Sale" on the sign.

The measurements are 36" inches (91.44 cm) Length, or tall X 24" inches (60.90 cm) Wide.

|
3
---- 24 ----
6
|

Sorry I wasn't more specific earlier. I'd like the elements of the sign to be scaled in size according to their importance, from largest to smallest:

My name: Derek Malloy
My phone number: 555-204-3967
My company name: Fern Hollow Realty
My license number: BRE 04827265 (This can be much smaller than the smallest text)
Additionally, please incorporate contemporary to mid-century modern elements on the wire frame roofline or a simple roof-like design.

Thank you!

Best regards,
Derek

```html
<!DOCTYPE html>
<html lang="en">
<head>
<meta charset="utf-8">
<title>Derek Malloy — Fern Hollow Realty Sign</title>
<link href="https://fonts.googleapis.com/css2?family=Bebas+Neue&family=Josefin+Sans:wght@600;700&family=Allura&display=swap" rel="stylesheet">
<style>
  :root {
    --board: #111214;
    --ink: #ffffff;
    --page: #ffffff;
    --roof-light: #3a3b3f;
    --roof-dark: #111214;
  }
  html, body {
    margin: 0;
    padding: 0;
    width: 1200px;
    height: 800px;
    overflow: hidden;
    background: var(--page);
  }
  .canvas {
    position: relative;
    width: 1200px;
    height: 800px;
  }
  .sign {
    position: absolute;
    left: 360px;
    top: 40px;
    width: 480px;
    height: 720px;
    background: var(--board);
    color: var(--ink);
  }
  .inner-frame {
    position: absolute;
    left: 30px;
    top: 30px;
    width: 420px;
    height: 660px;
    border: 5px solid var(--ink);
    box-sizing: border-box;
  }
  .roofline-art {
    position: absolute;
    left: 35px;
    width: 410px;
    height: 128px;
  }
  .roofline-top {
    top: 35px;
    background: linear-gradient(to bottom, var(--roof-dark) 0%, var(--roof-light) 55%, var(--roof-dark) 100%);
  }
  .roofline-bottom {
    top: 557px;
    background: linear-gradient(to bottom, var(--roof-dark) 0%, var(--roof-light) 55%, var(--roof-dark) 100%);
  }
  .sign-text {
    position: absolute;
    left: 0;
    width: 480px;
    text-align: center;
    margin: 0;
  }
  .agent-name {
    top: 238px;
    font-family: "Bebas Neue", "Oswald", sans-serif;
    font-weight: 400;
    font-size: 76px;
    letter-spacing: 1px;
    line-height: 1;
  }
  .agent-phone {
    top: 352px;
    font-family: "Josefin Sans", sans-serif;
    font-weight: 700;
    font-size: 36px;
    line-height: 1;
    display: flex;
    justify-content: center;
    align-items: baseline;
    gap: 12px;
  }
  .script-label {
    font-family: "Allura", cursive;
    font-weight: 400;
    font-size: 30px;
  }
  .company {
    top: 436px;
    left: 74px;
    width: 332px;
    height: 54px;
    border-top: 2px solid var(--ink);
    border-bottom: 2px solid var(--ink);
    box-sizing: border-box;
    display: flex;
    align-items: center;
    justify-content: center;
    font-family: "Josefin Sans", sans-serif;
    font-weight: 600;
    font-size: 28px;
    letter-spacing: 0.5px;
    padding-top: 5px;
  }
  .license {
    top: 512px;
    font-family: "Josefin Sans", sans-serif;
    font-weight: 700;
    font-size: 17px;
    letter-spacing: 1px;
    display: flex;
    justify-content: center;
    align-items: baseline;
    gap: 14px;
  }
  .license .script-label { font-size: 30px; }
</style>
</head>
<body>
<div class="canvas">
  <div class="sign">
    <div class="inner-frame"></div>
    <div class="roofline-art roofline-top" role="img" aria-label="White outline illustration of a row of house rooflines with small windows"></div>
    <div class="roofline-art roofline-bottom" role="img" aria-label="White outline illustration of a row of house rooflines with small windows"></div>

    <h1 class="sign-text agent-name">Derek Malloy</h1>
    <p class="sign-text agent-phone"><span class="script-label">Contact</span><span>555 204 3967</span></p>
    <p class="sign-text company">Fern Hollow Realty</p>
    <p class="sign-text license"><span class="script-label">License</span><span>BRE 04827265</span></p>
  </div>
</div>
</body>
</html>
```